Ledgerwise Business Card Design

Business Card Design for new business called Ledgerwise focused on selling business software to small and medium size companies who have outgrown Tallymark. Similar companies would be Tallymark, Nuvo, CoreFlow. Also Dealharbor would be good to look at for additional ideas around look and feel.

Target Market(s)

Business to Business

Industry/Entity Type

Information Technology

Contact Information for Business Card

Standard Business Card Information

Font styles to use
Sans Serif

```html
<!DOCTYPE html>
<html lang="en">
<head>
<meta charset="utf-8">
<title>Ledgerwise Business Card</title>
<link href="https://fonts.googleapis.com/css2?family=Open+Sans:wght@400;600;700;800&display=swap" rel="stylesheet">
<style>
  :root {
    --page: #e9e6e1;
    --orange: #f0821e;
    --orange-deep: #d9701a;
    --blue: #0e5a92;
    --blue-deep: #0a4676;
    --white: #ffffff;
    --ink: #ffffff;
  }
  * { box-sizing: border-box; margin: 0; padding: 0; }
  html, body { width: 1200px; height: 950px; overflow: hidden; }
  body {
    background: var(--page);
    font-family: "Open Sans", Arial, sans-serif;
    position: relative;
  }
  .card {
    position: absolute;
    width: 700px;
    height: 400px;
    border-radius: 4px;
    overflow: hidden;
    box-shadow: 0 10px 30px rgba(0,0,0,0.18);
  }
  /* Back of card */
  .card--back {
    left: 100px; top: 60px;
    background: linear-gradient(135deg, var(--orange) 0%, var(--orange-deep) 100%);
    display: flex; flex-direction: column;
    align-items: center; justify-content: center; gap: 18px;
  }
  .back-brand { display: flex; align-items: center; gap: 14px; }
  .back-brand__dot { width: 30px; height: 30px; border-radius: 50%; background: var(--white); }
  .back-brand__name {
    color: var(--white); font-weight: 800; font-size: 46px; letter-spacing: 1px; text-transform: uppercase;
  }
  .back-web { color: var(--white); font-size: 18px; letter-spacing: 2px; }

  /* Front of card */
  .card--front {
    left: 400px; top: 470px;
    background: var(--white);
  }
  .front-wave { position: absolute; inset: 0; width: 700px; height: 400px; }
  .front-brand {
    position: absolute; left: 250px; top: 82px;
    display: flex; align-items: center; gap: 12px;
  }
  .front-brand__name {
    color: var(--blue); font-weight: 800; font-size: 38px; letter-spacing: 0.5px; text-transform: uppercase;
  }
  .front-brand__dot { width: 26px; height: 26px; border-radius: 50%; background: var(--orange); }

  .contact {
    position: absolute; left: 130px; top: 232px;
    color: var(--ink); font-size: 17px; line-height: 27px;
  }
  .contact__name { color: var(--orange); font-weight: 700; font-size: 19px; padding-left: 60px; }
  .contact__title { color: var(--white); font-weight: 400; }
  .contact__label { color: var(--orange); font-weight: 700; }
  .contact__row--indent { padding-left: 18px; }
</style>
</head>
<body>

<section class="card card--back" aria-label="Card back">
  <div class="back-brand">
    <span class="back-brand__dot"></span>
    <span class="back-brand__name">Ledgerwise</span>
  </div>
  <div class="back-web">www.ledgerwise.co</div>
</section>

<section class="card card--front" aria-label="Card front">
  <svg class="front-wave" viewBox="0 0 700 400" aria-hidden="true">
    <path d="M0,200 Q360,100 700,390 L700,400 L0,400 Z" fill="var(--blue)"/>
    <path d="M0,200 Q360,100 700,390" fill="none" stroke="var(--orange)" stroke-width="9"/>
  </svg>

  <div class="front-brand">
    <span class="front-brand__name">Ledgerwise</span>
    <span class="front-brand__dot"></span>
  </div>

  <div class="contact">
    <div class="contact__name">MARCUS HALE &nbsp;- &nbsp;<span class="contact__title">PRESIDENT</span></div>
    <div class="contact__row">2217 Alder Court, Brookvale, NY 11820</div>
    <div class="contact__row contact__row--indent"><span class="contact__label">P :</span> 555 0142 7781 <span class="contact__label">F :</span> 555 0198 3364</div>
    <div class="contact__row"><span class="contact__label">E :</span> marcus@ledgerwise.co <span class="contact__label">W :</span> www.ledgerwise.co</div>
  </div>
</section>

</body>
</html>
```